REAL ESTATE MAILBOX DROP FLYER

I am looking for two flyer designs. One for DL and one for A4 size. My company is a boutique real estate agency that offers a full/high quality service at a very low commission rate.

Key Phrases to be included

A4 Design should have a space for some text and a table in the center (outline below)

Target Market(s)

Home Owners

Industry/Entity Type

Real Estate Agent

Colors
0455a3

Requirements
Must have
• Eye Catching
• Bold
• high end feel
• Color pallette should match the logo
• The feel of the brochures must convey a trustworthy, high end service.
• Must be eye catching and easy to read
• Editable file formats must be supplied

```html
<!DOCTYPE html>
<html lang="en">
<head>
<meta charset="utf-8">
<title>Keystone Lane Property – Real Estate Agent Flyer</title>
<link href="https://fonts.googleapis.com/css2?family=Bebas+Neue&family=Oswald:wght@200&family=Source+Sans+3:wght@400;600&family=Libre+Baskerville&display=swap" rel="stylesheet">
<style>
  :root {
    --navy: #062840;
    --blue: #0455a3;
    --slate: #58595b;
    --pill: #939598;
    --accent-red: #c8202f;
    --white: #ffffff;
    --black: #000000;
  }
  * { margin: 0; padding: 0; box-sizing: border-box; }
  html, body { width: 1200px; height: 2440px; overflow: hidden; background: var(--white); }
  .flyer { position: relative; width: 1200px; height: 2440px; overflow: hidden; background: var(--white); font-family: "Source Sans 3", sans-serif; }

  .top-band { position: absolute; left: 0; top: 0; width: 1200px; height: 205px; background: var(--navy); }
  .logo-panel { position: absolute; left: 375px; top: 76px; width: 450px; height: 200px; background: var(--white); }
  .brand-name {
    position: absolute; left: 375px; top: 150px; width: 450px; text-align: center;
    font-family: "Libre Baskerville", serif; color: var(--navy); font-size: 40px; line-height: 46px; letter-spacing: 1px;
  }
  .logo-rule { position: absolute; left: 422px; top: 301px; width: 355px; height: 27px; background: var(--navy); }

  .hero { position: absolute; left: 80px; top: 348px; width: 1040px; height: 710px; }
  .photo-circle { position: absolute; left: 0; top: 0; width: 1200px; height: 2440px; pointer-events: none; }

  .headline { position: absolute; right: 92px; text-align: right; line-height: 1; }
  .headline-real { top: 1093px; font-family: "Bebas Neue", sans-serif; font-size: 146px; color: var(--blue); }
  .headline-estate { top: 1196px; font-family: "Bebas Neue", sans-serif; font-size: 224px; color: var(--slate); letter-spacing: 2px; }
  .headline-agent { top: 1384px; font-family: "Oswald", sans-serif; font-weight: 200; font-size: 120px; color: var(--blue); letter-spacing: 1px; }
  .headline-rule { position: absolute; left: 629px; top: 1517px; width: 478px; height: 23px; background: var(--black); }

  .phrases-heading {
    position: absolute; left: 83px; top: 1733px; width: 547px; height: 52px;
    border-left: 8px solid var(--blue); border-right: 8px solid var(--blue);
    font-weight: 600; font-size: 37px; line-height: 52px; color: var(--blue); padding-left: 18px; white-space: nowrap;
  }
  .phrase {
    position: absolute; left: 94px; width: 523px; height: 98px; border-radius: 46px; background: var(--pill);
    color: var(--white); font-size: 31px; line-height: 33px; padding: 0 0 0 29px;
    display: flex; flex-direction: column; justify-content: center; white-space: nowrap;
  }
  .phrase .highlight { color: var(--accent-red); }
  .phrase-1 { top: 1811px; }
  .phrase-2 { top: 1920px; }
  .phrase-3 { top: 2029px; }

  .info-panel { position: absolute; left: 676px; top: 1645px; width: 384px; height: 486px; background: var(--navy); color: var(--white); font-size: 23px; }
  .info-label { position: absolute; left: 44px; line-height: 1; letter-spacing: 0.3px; }
  .info-top { top: 31px; }
  .info-top-rule { position: absolute; left: 32px; top: 62px; width: 319px; height: 3px; background: var(--white); }
  .info-box { position: absolute; left: 28px; width: 328px; border: 3px solid var(--white); }
  .info-box-text { top: 80px; height: 124px; }
  .info-box-table { top: 209px; height: 193px; }
  .info-box .info-label { left: 14px; top: 8px; }
  .info-bottom { top: 444px; }

  .footer { position: absolute; left: 0; top: 2166px; width: 1200px; height: 274px; background: var(--navy); color: var(--white); }
  .footer-title { position: absolute; left: 0; width: 1118px; top: 55px; text-align: center; font-size: 23px; letter-spacing: 0.3px; }
  .footer-divider { position: absolute; left: 555px; top: 91px; width: 7px; height: 51px; background: var(--white); }
  .footer-col { position: absolute; top: 92px; font-size: 20px; line-height: 29px; white-space: nowrap; }
  .footer-left { left: 169px; }
  .footer-right { left: 642px; }
</style>
</head>
<body>
<div class="flyer">
  <div class="top-band"></div>
  <div class="logo-panel"></div>
  <div class="brand-name">KEYSTONE LANE<br>PROPERTY</div>
  <div class="logo-rule"></div>

  <svg class="hero" viewBox="0 0 1040 710" aria-hidden="false">
    <defs>
      <linearGradient id="living-tones" x1="0" y1="0" x2="0" y2="1">
        <stop offset="0" stop-color="#e9eaec"/>
        <stop offset="0.45" stop-color="#dcdcdc"/>
        <stop offset="0.7" stop-color="#c9b9a2"/>
        <stop offset="1" stop-color="#a98a64"/>
      </linearGradient>
    </defs>
    <path d="M0 0 H1040 V405 Q 900 585 682 710 L 560 640 Q 300 590 0 618 Z" fill="var(--navy)"/>
    <path d="M2 18 H1037 V400 Q 895 572 682 692 L 560 626 Q 300 578 2 604 Z" fill="url(#living-tones)" role="img" aria-label="Photo of a bright open-plan living room with kitchen and lounge"/>
  </svg>

  <svg class="photo-circle" viewBox="0 0 1200 2440">
    <defs>
      <linearGradient id="bedroom-tones" x1="0" y1="0" x2="0" y2="1">
        <stop offset="0" stop-color="#eceef0"/>
        <stop offset="0.55" stop-color="#d8dbe0"/>
        <stop offset="1" stop-color="#5e5f63"/>
      </linearGradient>
      <linearGradient id="dining-tones" x1="0" y1="0" x2="0" y2="1">
        <stop offset="0" stop-color="#f1f1f1"/>
        <stop offset="0.5" stop-color="#cfcac3"/>
        <stop offset="1" stop-color="#a9a6a2"/>
      </linearGradient>
    </defs>
    <circle cx="366" cy="1112" r="264" fill="var(--white)"/>
    <circle cx="366" cy="1110" r="239" fill="url(#bedroom-tones)" role="img" aria-label="Photo of a styled master bedroom"/>
    <circle cx="264" cy="1508" r="180" fill="url(#dining-tones)" role="img" aria-label="Photo of a lounge and dining area"/>
  </svg>

  <div class="headline headline-real">REAL</div>
  <div class="headline headline-estate">ESTATE</div>
  <div class="headline headline-agent">AGENT</div>
  <div class="headline-rule"></div>

  <div class="phrases-heading">KEY PHRASES – Eye Catching</div>
  <div class="phrase phrase-1"><span>Full Service Agency,</span><span class="highlight">1% Commission</span></div>
  <div class="phrase phrase-2"><span>Contact Marcus today on</span><span>0400 318 927 for a <span class="highlight">FREE APPRAISAL!</span></span></div>
  <div class="phrase phrase-3"><span>Save Thousands On Commissions!</span></div>

  <div class="info-panel">
    <div class="info-label info-top">ARTWORK/LOGOS ETC</div>
    <div class="info-top-rule"></div>
    <div class="info-box info-box-text"><div class="info-label">WRITTEN TEXT</div></div>
    <div class="info-box info-box-table"><div class="info-label">TABLE/INFORMATION</div></div>
    <div class="info-label info-bottom">ARTWORK/LOGOS ETC</div>
  </div>

  <footer class="footer">
    <div class="footer-title">CONTACT DETAILS</div>
    <div class="footer-col footer-left">More Money in YOUR Pocket!<br>Marcus Ellery - 0400 318 927</div>
    <div class="footer-divider"></div>
    <div class="footer-col footer-right">marcus@keystonelaneproperty.com.au<br>www.keystonelaneproperty.com.au</div>
  </footer>
</div>
</body>
</html>
```